Brantley Yard Services Flyer Design

I need a new flyer design for my business, Brantley Yard Services. I’ll be providing my old flyer and logo as references. The new flyer should feature updated wording, contact information, logos, and photos, but still keep the original “What We Do” section and include the phrase “Don’t See? Just Ask!” somewhere near the services. The flyer needs to look great in black and white for door-to-door handouts but also be eye-catching and professional enough for social media use.

The updated content should include the headline “Transforming Outdoor Spaces with Hard Work & Precision” and highlight three main service areas: Landscaping Services (project-based landscaping to clean, prepare, and transform outdoor spaces with precision), Property Cleanup (quick hauls, debris removal, or full cleanouts—no job too big or small), and Ground Preparation (pad preparation, brush removal, and fire lines—making properties safe, functional, and project-ready).

Please also include a “Why Choose Us?” section that lists: Locally owned since 2022, Reliable & affordable – no corners cut, Professional results you can trust, LICENSED AND Insured, and Quality work / on time / references / flexible / follow-up.

At the bottom, include the contact details: Call or Text Today!
www.brantleyyard.example
| sales@brantleyyard.example
| (555) 014-2793

The overall design should be clean, professional, and easy to read with a layout that clearly shows what we offer. Use visuals that represent outdoor services, landscaping, and property cleanup/prep work. I want something that feels trustworthy, family-friendly, and modern.
Use the same photo of leaf clean up from the original flyer if possible.
Our company colors are also black and white. For the most part.

```html
<!DOCTYPE html>
<html lang="en">
<head>
<meta charset="utf-8">
<title>Brantley Yard Services Flyer</title>
<link href="https://fonts.googleapis.com/css2?family=Poppins:wght@400;500;600;700&family=Bebas+Neue&display=swap" rel="stylesheet">
<style>
  :root {
    --ink: #111111;
    --band: #1f1f1f;
    --paper: #ffffff;
    --canvas: #ffffff;
    --leaf-dark: #6b3a14;
    --leaf-mid: #b8651c;
    --leaf-light: #e0a13a;
  }
  * { box-sizing: border-box; margin: 0; padding: 0; }
  html, body { width: 1200px; height: 1013px; overflow: hidden; background: var(--canvas); }
  body { font-family: "Poppins", sans-serif; color: var(--ink); }

  .flyer {
    position: absolute; left: 217px; top: 0;
    width: 766px; height: 1013px;
    background: var(--paper); overflow: hidden;
  }
  .hero-band { position: absolute; left: 0; top: 0; width: 766px; height: 467px; background: var(--band); }
  .hero-photo {
    position: absolute; left: 280px; top: 0; width: 486px; height: 467px;
    background:
      radial-gradient(ellipse at 70% 45%, var(--leaf-light) 0%, var(--leaf-mid) 40%, var(--leaf-dark) 80%),
      var(--leaf-mid);
    -webkit-mask-image: linear-gradient(to right, transparent 0%, #000 35%);
    mask-image: linear-gradient(to right, transparent 0%, #000 35%);
  }

  .brand {
    position: absolute; left: 37px; top: 48px;
    display: flex; align-items: center; gap: 10px;
    color: var(--paper); font-weight: 700; font-size: 22px; line-height: 1;
  }
  .brand-mark { width: 30px; height: 30px; background: var(--paper); }

  .headline {
    position: absolute; left: 37px; top: 132px;
    color: var(--paper); font-weight: 700; font-size: 42px; line-height: 46px;
    letter-spacing: -0.3px;
  }

  .work-photo {
    position: absolute; top: 344px; height: 228px; width: 333px;
    border: 2px solid var(--ink);
  }
  .work-photo.site { left: 38px; background: linear-gradient(to bottom, #b9c6d6 0%, #8d8f92 38%, #a39a8c 60%, #6f6a64 100%); }
  .work-photo.haul { left: 398px; background: linear-gradient(to bottom, #9a7d5a 0%, #5c5a55 35%, #7d7a6f 65%, #2e3a5a 100%); }

  .tag {
    position: absolute; background: var(--ink); color: var(--paper);
    font-weight: 700; display: flex; align-items: center; justify-content: center;
    white-space: nowrap;
  }
  .tag.what { left: 38px; top: 596px; width: 228px; height: 37px; font-size: 24px; }
  .tag.why { left: 481px; top: 596px; width: 251px; height: 37px; font-size: 24px; }
  .tag.phone { left: 498px; top: 748px; width: 234px; height: 38px; font-size: 26px; font-weight: 600; }
  .tag.licensed { left: 222px; top: 879px; width: 323px; height: 38px; font-size: 24px; }

  .divider { position: absolute; left: 383px; top: 592px; width: 2px; height: 256px; background: var(--ink); }

  .services { position: absolute; left: 37px; top: 640px; width: 320px; }
  .service h3 { font-size: 20px; font-weight: 700; line-height: 24px; white-space: nowrap; }
  .service p { font-size: 13px; line-height: 13.5px; margin-bottom: 6px; white-space: nowrap; }
  .ask {
    position: absolute; left: 37px; top: 826px;
    font-family: "Bebas Neue", sans-serif; font-size: 23px; line-height: 26px;
  }

  .reasons {
    position: absolute; right: 36px; top: 655px; list-style: none;
    text-align: right; font-size: 14px; line-height: 25px; white-space: nowrap;
  }
  .reasons li::after { content: "\2022"; margin-left: 6px; font-size: 15px; }

  .cta {
    position: absolute; right: 36px; top: 788px;
    font-family: "Bebas Neue", sans-serif; font-size: 29px; line-height: 32px;
  }

  .values {
    position: absolute; left: 0; width: 766px; top: 930px;
    text-align: center; font-size: 21px; line-height: 28px;
  }

  .contact-bar {
    position: absolute; left: 0; top: 973px; width: 766px; height: 40px;
    background: var(--ink); color: var(--paper);
    display: flex; align-items: center; justify-content: space-between; padding: 0 36px;
    font-size: 17px; white-space: nowrap;
  }
  .contact-item { display: flex; align-items: center; gap: 6px; }
  .contact-item.phone-line { font-size: 15px; }
  .contact-item svg { width: 20px; height: 20px; flex: none; }
</style>
</head>
<body>
<main class="flyer">
  <div class="hero-band"></div>
  <div class="hero-photo" role="img" aria-label="Photo of a rake in a pile of autumn leaves"></div>

  <div class="brand"><span class="brand-mark"></span>Brantley Yard Services</div>

  <h1 class="headline">Transforming<br>Outdoor Spaces<br>with Hard Work<br>&amp; Precision</h1>

  <div class="work-photo site" role="img" aria-label="Photo of a paver driveway job site with a truck and excavator"></div>
  <div class="work-photo haul" role="img" aria-label="Photo of a trailer loaded with cleanout debris"></div>

  <div class="tag what">WHAT WE DO</div>
  <div class="divider"></div>

  <section class="services">
    <div class="service">
      <h3>Landscaping Services</h3>
      <p>project-based landscaping to clean, prepare,<br>and transform outdoor spaces with precision</p>
    </div>
    <div class="service">
      <h3>Property Cleanup</h3>
      <p>quick hauls, debris removal, or full cleanouts<br>no job too big or small</p>
    </div>
    <div class="service">
      <h3>Ground Preparation</h3>
      <p>pad preparation, brush removal, and fire lines<br>making properties safe,<br>functional, and project-ready</p>
    </div>
  </section>
  <div class="ask">+Don't see it, just ask</div>

  <div class="tag why">WHY CHOOSE US?</div>
  <ul class="reasons">
    <li>Locally owned since 2022</li>
    <li>Reliable &amp; affordable – no corners cut</li>
    <li>Professional results you can trust</li>
  </ul>
  <div class="tag phone">(555) 014-2793</div>
  <div class="cta">Call or text today!</div>

  <div class="tag licensed">LICENSED AND INSURED</div>
  <p class="values">Quality work | on time | references | flexible | follow-up</p>

  <footer class="contact-bar">
    <span class="contact-item">
      <svg viewBox="0 0 24 24" fill="none" stroke="currentColor" stroke-width="1.6"><circle cx="12" cy="12" r="10"/><ellipse cx="12" cy="12" rx="4.5" ry="10"/><path d="M2 12h20M4 7h16M4 17h16"/></svg>
      www.brantleyyard.example
    </span>
    <span class="contact-item phone-line">
      <svg viewBox="0 0 24 24"><circle cx="12" cy="12" r="11" fill="currentColor"/><path d="M8.5 6.5l2 2-1.2 1.5c.8 1.8 2 3 3.8 3.8l1.5-1.2 2 2-1.4 1.9c-3.8-.4-7.3-3.9-7.7-7.7z" fill="#111"/></svg>
      (555) 014-2793
    </span>
    <span class="contact-item">
      <svg viewBox="0 0 24 24" fill="none" stroke="currentColor" stroke-width="1.6"><circle cx="12" cy="12" r="10"/><rect x="6.5" y="8" width="11" height="8"/><path d="M6.5 8l5.5 4.5L17.5 8M6.5 16l4-4M17.5 16l-4-4"/></svg>
      sales@brantleyyard.example
    </span>
  </footer>
</main>
</body>
</html>
```